my personal cards just intrducing my self

Massage Therapy to get my name out their

Target Market(s)

40 year olds who enjoy massage

Industry/Entity Type

Massage

Contact Information for Business Card

Marcus L Tolhaven
LMT-Licensed Massage Therapist
*Swedish *Deep Tissue *Prenatal
*Reflexology *Chair and more

(738)-462-1937
marcustolhaven@mailbrook.net

Font styles to use
Serif

Colors
0456a4
6b449b

```html
<!DOCTYPE html>
<html lang="en">
<head>
<meta charset="UTF-8">
<title>Marcus L Tolhaven — Business Cards</title>
<link href="https://fonts.googleapis.com/css2?family=Alfa+Slab+One&family=Roboto+Condensed:wght@300;700&family=Roboto:wght@300;400;700&display=swap" rel="stylesheet">
<style>
  :root {
    --page-bg: #dcdadb;
    --card-dark: #0d1a21;
    --card-mid: #16303b;
    --accent-blue: #2aa2e6;
    --text-light: #e4ecf0;
    --text-soft: #aebcc4;
    --rule: #5d7480;
    --slab-grey: #b7bec3;
  }
  * { margin: 0; padding: 0; box-sizing: border-box; }
  html, body { width: 1200px; height: 800px; overflow: hidden; }
  body {
    background: var(--page-bg);
    position: relative;
  }
  .card {
    position: absolute;
    top: 246px;
    width: 540px;
    height: 308px;
    border-radius: 48px 0 0 0;
    background: linear-gradient(150deg, var(--card-mid) 0%, var(--card-dark) 65%);
    overflow: hidden;
    box-shadow: 0 10px 26px rgba(0,0,0,0.25);
  }
  .card--services { left: 40px; }
  .card--contact { left: 620px; }

  /* Services side */
  .services-list {
    position: absolute;
    left: 40px;
    top: 34px;
    width: 460px;
    height: 250px;
  }
  .services-list text {
    font-family: "Alfa Slab One", serif;
    fill: var(--slab-grey);
  }
  .services-list .and-more {
    font-family: "Roboto Condensed", sans-serif;
    font-weight: 700;
    fill: var(--text-light);
  }

  /* Contact side */
  .identity {
    position: absolute;
    right: 34px;
    top: 58px;
    text-align: right;
  }
  .identity__name {
    font-family: "Roboto Condensed", sans-serif;
    font-size: 31px;
    letter-spacing: 0.5px;
    text-transform: uppercase;
    line-height: 1;
  }
  .identity__first { color: var(--accent-blue); font-weight: 700; }
  .identity__last { color: var(--accent-blue); font-weight: 300; }
  .identity__title {
    font-family: "Roboto", sans-serif;
    font-weight: 300;
    font-size: 14px;
    color: var(--text-light);
    margin-top: 6px;
  }
  .contact-row {
    position: absolute;
    display: flex;
    align-items: center;
    gap: 10px;
    font-family: "Roboto", sans-serif;
    color: var(--text-light);
  }
  .contact-row--phone { left: 196px; top: 150px; font-size: 15px; font-weight: 700; }
  .contact-row--email { left: 60px; top: 198px; font-size: 14px; font-weight: 300; }
  .contact-row svg { fill: var(--accent-blue); flex: none; }
  .rule {
    position: absolute;
    height: 1px;
    background: var(--rule);
  }
  .rule--upper { left: 56px; width: 430px; top: 180px; }
  .rule--lower { left: 56px; width: 430px; top: 228px; }
</style>
</head>
<body>

  <section class="card card--services" aria-label="Services side">
    <svg class="services-list" viewBox="0 0 460 250" aria-label="Swedish, Deep Tissue, Prenatal Reflexology, Sports and more">
      <text x="0" y="56" font-size="62" textLength="460" lengthAdjust="spacingAndGlyphs">SWEDISH</text>
      <text x="0" y="106" font-size="48" textLength="460" lengthAdjust="spacingAndGlyphs">DEEP TISSUE</text>
      <text x="0" y="140" font-size="30" textLength="460" lengthAdjust="spacingAndGlyphs">PRENATAL REFLEXOLOGY</text>
      <text x="0" y="206" font-size="64" textLength="460" lengthAdjust="spacingAndGlyphs">SPORTS</text>
      <text class="and-more" x="340" y="236" font-size="16" textLength="120" lengthAdjust="spacing">AND MORE......</text>
    </svg>
  </section>

  <section class="card card--contact" aria-label="Contact side">
    <div class="identity">
      <h1 class="identity__name"><span class="identity__first">Marcus</span> <span class="identity__last">L Tolhaven</span></h1>
      <p class="identity__title">LMT-Licensed Massage Therapist</p>
    </div>

    <div class="contact-row contact-row--phone">
      <svg width="13" height="13" viewBox="0 0 24 24" aria-hidden="true"><path d="M6.6 10.8a15.1 15.1 0 0 0 6.6 6.6l2.2-2.2c.3-.3.7-.4 1-.2 1.1.4 2.3.6 3.6.6.6 0 1 .4 1 1V20c0 .6-.4 1-1 1A17 17 0 0 1 3 4c0-.6.4-1 1-1h3.5c.6 0 1 .4 1 1 0 1.3.2 2.5.6 3.6.1.3 0 .7-.2 1z"/></svg>
      <span>(738)-462-1937</span>
    </div>
    <div class="rule rule--upper"></div>

    <div class="contact-row contact-row--email">
      <svg width="14" height="11" viewBox="0 0 24 18" aria-hidden="true"><path d="M0 0h24v18H0z M2 2v1l10 7 10-7V2z" fill-rule="evenodd"/></svg>
      <span>marcustolhaven@mailbrook.net</span>
    </div>
    <div class="rule rule--lower"></div>
  </section>

</body>
</html>
```